Brookmere Osteopathy flyer

I want a clean clear DL flyer (but also want an A4 poster) promoting a new Osteopathic business in a semi rural area in Tasmania (Australia).
It can have pictures like the examples attached to show people what Osteopathy is (its like Chiropractic and physiotherapy).
I am the sole practioner and am male, so any pictures would be best to be a white male if possible.
I've attached some wording, you can use all, or none of it
I don't have a phone number for the business yet
info@brookmereosteopathy.example
www.brookmereosteopathy.example
Target Market(s)
Australians, from tradies, professionals, babies to retired people
Industry/Entity Type
Health
Look and feel

```html
<!DOCTYPE html>
<html lang="en">
<head>
<meta charset="utf-8">
<title>Brookmere Osteopathy – DL Flyer</title>
<link href="https://fonts.googleapis.com/css2?family=Oswald:wght@400&family=Saira+Condensed:wght@600;700&family=Lexend:wght@300;400;500&display=swap" rel="stylesheet">
<style>
  :root {
    --blue: #1689cd;
    --orange: #f39a2e;
    --ink: #1f1f22;
    --paper: #ffffff;
    --stage: #ececec;
    --photo-warm: linear-gradient(150deg, #e9e4df 0%, #cfc4ba 55%, #9fb8c9 100%);
    --photo-cool: linear-gradient(160deg, #cfd3d6 0%, #b9b2aa 55%, #8f8a86 100%);
  }
  * { box-sizing: border-box; margin: 0; padding: 0; }
  html, body { width: 1191px; height: 1200px; overflow: hidden; }
  body { background: var(--stage); position: relative; font-family: "Lexend", sans-serif; color: var(--ink); }

  .flyer { position: absolute; top: 87px; width: 482px; height: 1026px; background: var(--paper); overflow: hidden; box-shadow: 0 2px 10px rgba(0,0,0,.12); }
  .flyer--front { left: 98px; }
  .flyer--back { left: 610px; }
  .flyer > * { position: absolute; }

  .corner { background: var(--blue); }
  .corner--accent { background: var(--orange); }

  .photo { display: block; }

  .brand { display: flex; flex-direction: column; align-items: center; justify-content: center; gap: 8px; text-align: center; }
  .brand__dot { width: 46px; height: 46px; border-radius: 50%; background: var(--blue); }
  .brand__name { font-family: "Lexend", sans-serif; font-weight: 500; font-size: 15px; line-height: 1.2; color: var(--blue); }

  .services-title { font-family: "Oswald", sans-serif; font-weight: 400; font-size: 29px; line-height: 34px; color: var(--ink); text-transform: uppercase; }

  .offer { font-family: "Saira Condensed", sans-serif; font-weight: 700; color: var(--blue); line-height: 1; text-transform: uppercase; }
  .offer__lead { display: block; font-size: 39px; }
  .offer__main { display: block; font-size: 62px; margin-top: 4px; }
  .offer__tail { display: block; font-size: 30px; margin-top: 2px; }

  .intro { font-size: 11.2px; line-height: 22px; font-weight: 300; color: var(--ink); }

  .footer { left: 0; bottom: 0; width: 100%; height: 91px; background: var(--blue); }
  .contact-list { list-style: none; color: #fff; font-size: 10.4px; font-weight: 400; }
  .contact-list li { display: flex; align-items: center; gap: 8px; height: 19.5px; }
  .contact-list svg { width: 10px; height: 10px; flex: none; }
  .phone { display: flex; align-items: center; gap: 12px; color: #fff; font-family: "Saira Condensed", sans-serif; font-weight: 600; font-size: 30px; }
  .phone svg { width: 30px; height: 34px; }

  .region { font-family: "Oswald", sans-serif; font-size: 21px; line-height: 33px; color: var(--ink); text-transform: uppercase; }

  .reasons-title { font-family: "Saira Condensed", sans-serif; font-weight: 700; font-size: 47px; line-height: 53px; color: var(--blue); }

  .reasons { list-style: none; }
  .reasons li { display: flex; align-items: center; height: 46px; font-size: 19.5px; font-weight: 500; color: var(--ink); }
  .reasons svg { width: 20px; height: 14px; margin-right: 13px; flex: none; }

  .slogan { font-family: "Saira Condensed", sans-serif; font-weight: 600; font-size: 33px; line-height: 38px; color: #fff; }
</style>
</head>
<body>

<!-- Front side -->
<section class="flyer flyer--front">
  <div class="corner" style="left:360px;top:0;width:122px;height:19px"></div>
  <div class="corner" style="left:456px;top:0;width:26px;height:99px"></div>

  <div class="brand" style="left:14px;top:30px;width:145px;height:125px">
    <span class="brand__dot"></span>
    <span class="brand__name">Brookmere<br>Osteopathy</span>
  </div>

  <div class="photo" role="img" aria-label="Practitioner assessing a patient's upper back and shoulder" style="left:209px;top:19px;width:247px;height:298px;background:var(--photo-warm)"></div>

  <h2 class="services-title" style="left:15px;top:190px">Chiropractic<br>and<br>Physiotherapy</h2>

  <div class="photo" role="img" aria-label="Patient lying on a treatment table receiving neck treatment" style="left:0;top:318px;width:211px;height:146px;background:linear-gradient(120deg,#e8ecef 0%,#c9c1b8 60%,#9aa3ab 100%)"></div>

  <h1 class="offer" style="left:225px;top:328px">
    <span class="offer__lead">Free Intial</span>
    <span class="offer__main">Physio</span>
    <span class="offer__tail">Consultation</span>
  </h1>

  <p class="intro" style="left:13px;top:470px;width:460px">Brookmere Osteopathy use a tailored combination of joint mobilisation/manipulation, stretching, movement, trigger point dry needling and targeted massage to reduce pain and restore optimal function. Hands-on treatment is backed up with rehabilitative exercise prescription and advice. So whether you're recovering from injury or managing chronic discomfort, we're here to help you move better and feel your best.</p>

  <div class="footer"></div>

  <div class="photo" role="img" aria-label="Gentle hands-on treatment for a sleeping baby" style="left:11px;top:609px;width:220px;height:157px;background:linear-gradient(160deg,#c9c3d6 0%,#a9b8cc 55%,#6ea8cf 100%)"></div>
  <div class="photo" role="img" aria-label="Practitioner treating a patient's lower back" style="left:241px;top:609px;width:221px;height:157px;background:linear-gradient(150deg,#e7e4e0 0%,#d8b993 55%,#5f7f94 100%)"></div>
  <div class="photo" role="img" aria-label="Practitioner explaining a spine model" style="left:12px;top:774px;width:220px;height:174px;background:linear-gradient(160deg,#f1f2f3 0%,#e2dccd 60%,#cdd3d8 100%)"></div>
  <div class="photo" role="img" aria-label="Osteopath performing a side-lying spinal technique" style="left:243px;top:774px;width:220px;height:174px;background:var(--photo-cool)"></div>

  <ul class="contact-list" style="left:16px;top:959px">
    <li><svg viewBox="0 0 10 10"><path d="M5 0.5a3.3 3.3 0 0 0-3.3 3.3C1.7 6.3 5 9.5 5 9.5s3.3-3.2 3.3-5.7A3.3 3.3 0 0 0 5 .5zm0 4.6a1.3 1.3 0 1 1 0-2.6 1.3 1.3 0 0 1 0 2.6z" fill="var(--orange)"/></svg>24 Willow Bend Road, Brookmere</li>
    <li><svg viewBox="0 0 10 10"><rect x="0.7" y="2" width="8.6" height="6.2" rx="0.8" fill="none" stroke="var(--orange)" stroke-width="1.2"/><path d="M1 2.5l4 3 4-3" fill="none" stroke="var(--orange)" stroke-width="1.2"/></svg>info@brookmereosteopathy.example</li>
    <li><svg viewBox="0 0 10 10"><circle cx="5" cy="5" r="4.2" fill="none" stroke="var(--orange)" stroke-width="1"/><ellipse cx="5" cy="5" rx="1.8" ry="4.2" fill="none" stroke="var(--orange)" stroke-width="0.9"/><path d="M0.8 5h8.4" stroke="var(--orange)" stroke-width="0.9"/></svg>www.brookmereosteopathy.example</li>
  </ul>

  <div class="phone" style="left:260px;top:961px">
    <svg viewBox="0 0 30 34"><path d="M8 6c-2 1-4 3-3 7 2 7 7 13 13 16 3 1 5 0 7-2l-4-5-3 2c-3-2-6-6-7-9l3-2-4-7z" fill="none" stroke="var(--orange)" stroke-width="2" stroke-linejoin="round"/><path d="M17 5a8 8 0 0 1 7 7M17 1a12 12 0 0 1 11 11" fill="none" stroke="var(--orange)" stroke-width="2" stroke-linecap="round"/></svg>
    03 5550 0142
  </div>
</section>

<!-- Back side -->
<section class="flyer flyer--back">
  <div class="corner corner--accent" style="left:0;top:0;width:122px;height:19px"></div>
  <div class="corner corner--accent" style="left:0;top:0;width:25px;height:99px"></div>

  <div class="photo" role="img" aria-label="Osteopath performing a side-lying spinal technique on a treatment table" style="left:25px;top:19px;width:247px;height:298px;background:var(--photo-cool)"></div>

  <div class="brand" style="left:292px;top:60px;width:145px;height:130px">
    <span class="brand__dot"></span>
    <span class="brand__name">Brookmere<br>Osteopathy</span>
  </div>

  <p class="region" style="left:294px;top:218px">Serving semi rural<br>area in Tasmania,<br>Australia</p>

  <h2 class="reasons-title" style="left:20px;top:350px">Common Reasons People<br>Visit An Osteopath</h2>

  <ul class="reasons" style="left:20px;top:455px">
    <li><svg viewBox="0 0 20 14"><path d="M1 13C3 7 8 5 14 5" fill="none" stroke="var(--orange)" stroke-width="3" stroke-linecap="round"/><path d="M12 1l7 4-7 4z" fill="var(--orange)"/></svg>Back / Neck Pain</li>
    <li><svg viewBox="0 0 20 14"><path d="M1 13C3 7 8 5 14 5" fill="none" stroke="var(--orange)" stroke-width="3" stroke-linecap="round"/><path d="M12 1l7 4-7 4z" fill="var(--orange)"/></svg>Headaches / Migraines</li>
    <li><svg viewBox="0 0 20 14"><path d="M1 13C3 7 8 5 14 5" fill="none" stroke="var(--orange)" stroke-width="3" stroke-linecap="round"/><path d="M12 1l7 4-7 4z" fill="var(--orange)"/></svg>Joint And Muscle Pain</li>
    <li><svg viewBox="0 0 20 14"><path d="M1 13C3 7 8 5 14 5" fill="none" stroke="var(--orange)" stroke-width="3" stroke-linecap="round"/><path d="M12 1l7 4-7 4z" fill="var(--orange)"/></svg>Pregnancy-related Discomfort</li>
    <li><svg viewBox="0 0 20 14"><path d="M1 13C3 7 8 5 14 5" fill="none" stroke="var(--orange)" stroke-width="3" stroke-linecap="round"/><path d="M12 1l7 4-7 4z" fill="var(--orange)"/></svg>Disc Related Issues</li>
    <li><svg viewBox="0 0 20 14"><path d="M1 13C3 7 8 5 14 5" fill="none" stroke="var(--orange)" stroke-width="3" stroke-linecap="round"/><path d="M12 1l7 4-7 4z" fill="var(--orange)"/></svg>Sciatica</li>
    <li><svg viewBox="0 0 20 14"><path d="M1 13C3 7 8 5 14 5" fill="none" stroke="var(--orange)" stroke-width="3" stroke-linecap="round"/><path d="M12 1l7 4-7 4z" fill="var(--orange)"/></svg>Plantar Fasciitis</li>
    <li><svg viewBox="0 0 20 14"><path d="M1 13C3 7 8 5 14 5" fill="none" stroke="var(--orange)" stroke-width="3" stroke-linecap="round"/><path d="M12 1l7 4-7 4z" fill="var(--orange)"/></svg>Tendonitis / Bursitis</li>
    <li><svg viewBox="0 0 20 14"><path d="M1 13C3 7 8 5 14 5" fill="none" stroke="var(--orange)" stroke-width="3" stroke-linecap="round"/><path d="M12 1l7 4-7 4z" fill="var(--orange)"/></svg>Adhesive Capsulitis (Frozen Shoulder)</li>
    <li><svg viewBox="0 0 20 14"><path d="M1 13C3 7 8 5 14 5" fill="none" stroke="var(--orange)" stroke-width="3" stroke-linecap="round"/><path d="M12 1l7 4-7 4z" fill="var(--orange)"/></svg>Tennis / Golfers Elbow</li>
  </ul>

  <div class="footer"></div>
  <p class="slogan" style="left:20px;top:944px">Move Better,<br>Feel Better.</p>
  <div class="phone" style="left:260px;top:958px">
    <svg viewBox="0 0 30 34"><path d="M8 6c-2 1-4 3-3 7 2 7 7 13 13 16 3 1 5 0 7-2l-4-5-3 2c-3-2-6-6-7-9l3-2-4-7z" fill="none" stroke="var(--orange)" stroke-width="2" stroke-linejoin="round"/><path d="M17 5a8 8 0 0 1 7 7M17 1a12 12 0 0 1 11 11" fill="none" stroke="var(--orange)" stroke-width="2" stroke-linecap="round"/></svg>
    03 5550 0142
  </div>
</section>

</body>
</html>
```